Web Page for marketing online agency

We are an online marketing agency that is acing the direct response model. We engage with our customers throughout different marketing techniques as research copy-writing, advertisements and content writing. We would need a website design that will have four main aspects: The Vision; stating who we are, The Mission; stating what we do, The Team And It's Values, and a Contact Form. For this design we would want a sharp, clean and smart approach, with illustrated elements or suggestive images. You can use the attached copy, the logo, the USP and the motto. Please integrate them as you see fit while keeping in mind the previous needs and copy. This website is going to be our connection with our possible partners, future colleagues and even our clients. You may submit a design for one page or integrate the 4 different aspects on separate web pages.
Target Market(s)
business partners, future employees, age range 25-60
Industry/Entity Type
Direct Marketing
Number of Pages Required
1 page
Requirements
Must have
- Menu / Header
- 4 Parts or 4 Pages including: vision, mission, team, contact
- Logo
- Motto: Direct Brilliance
- USP: We help people help themselves.
- The copy attached
Nice to have
- Representative illustrated images or elements
Should not have
- A boring design, classical design - Pagequill like

```html
<!DOCTYPE html>
<html lang="en">
<head>
<meta charset="utf-8">
<title>Brightlane — Direct Brilliance</title>
<link href="https://fonts.googleapis.com/css2?family=Poppins:wght@300;400;500;600&display=swap" rel="stylesheet">
<style>
:root{
  --blue:#2ea3dc;
  --blue-dark:#1f7fae;
  --ink:#1d1d1d;
  --text:#555;
  --muted:#8a8a8a;
  --rule:#d9d9d9;
  --tile:#e6e6e4;
  --dark:#353535;
  --darker:#2c2c2c;
  --footer:#0d0d0d;
  --white:#fff;
}
*{box-sizing:border-box;margin:0;padding:0}
html,body{width:1200px;height:3214px;overflow:hidden}
body{font-family:"Poppins",Arial,sans-serif;color:var(--text);background:var(--white);position:relative}
.abs{position:absolute}

.top-rule{left:0;top:0;width:1200px;height:5px;background:var(--blue)}
.header{left:0;top:5px;width:1200px;height:113px}
.brand{left:86px;top:40px}
.brand-name{font-size:40px;font-weight:600;color:var(--ink);letter-spacing:-0.5px}
.header-contact{right:88px;top:22px;display:flex;gap:38px;font-size:15px;color:var(--ink)}
.header-contact span{display:flex;align-items:center;gap:10px}
.header-contact svg{width:18px;height:18px}
.nav{right:88px;top:78px;display:flex;font-size:16px;color:var(--ink)}
.nav a{color:inherit;text-decoration:none;padding:0 38px;border-left:1px solid #999;line-height:16px}
.nav a:first-child{border-left:0;padding-left:0}
.nav a:last-child{padding-right:0}
.nav-line{right:88px;top:62px;width:560px;height:1px;background:var(--rule)}

.hero{left:0;top:118px;width:1200px;height:658px;background:linear-gradient(120deg,#7b6a5c 0%,#c9b9a6 40%,#e9e3da 60%,#8a7766 100%)}

.section-title{left:0;width:1200px;text-align:center;font-weight:400;color:var(--ink)}
.subtitle{left:0;width:1200px;display:flex;justify-content:center;align-items:center;gap:36px;font-size:30px;font-weight:300;color:#6a6a6a}
.subtitle i{display:block;width:280px;height:1px;background:var(--rule)}

.lead{left:90px;width:1020px;text-align:center;font-size:16.5px;font-weight:500;line-height:34px;color:var(--ink)}
.body-copy{left:80px;width:1040px;text-align:center;font-size:13.5px;line-height:35px;color:var(--muted)}
.btn{display:flex;align-items:center;justify-content:center;background:var(--blue);color:var(--white);border-radius:30px;font-size:20px;font-weight:400}
.learn-more{left:499px;top:1230px;width:202px;height:54px}

.values{left:86px;top:1341px;display:flex;gap:43px}
.value{width:171px;height:142px;background:var(--tile);display:flex;flex-direction:column;align-items:center;justify-content:flex-end;padding-bottom:22px;gap:14px;color:var(--ink);font-size:21px;font-weight:500}
.value svg{width:62px;height:62px;fill:none;stroke:#888;stroke-width:2.4}

.mission-photo{left:0;top:1528px;width:585px;height:375px;background:linear-gradient(135deg,#3b4a5a 0%,#a58564 45%,#d9cfc3 75%,#f2efea 100%)}
.mission-panel{left:613px;top:1528px;width:587px;height:375px;background:var(--blue);color:var(--white);padding:36px 62px}
.mission-panel h2{font-size:32px;font-weight:500}
.mission-panel h3{font-size:19px;font-weight:300;letter-spacing:2px;margin-top:12px}
.mission-panel .rule{width:115px;height:1px;background:rgba(255,255,255,.6);margin:24px 0 30px}
.mission-panel p{font-size:14px;line-height:25px;width:450px}
.mission-panel .btn{width:190px;height:52px;background:var(--blue-dark);margin-top:38px}

.team-intro{left:90px;width:1020px;top:2144px;text-align:center;font-size:13.5px;line-height:29px;color:#777}
.member{top:2261px;display:flex;gap:37px}
.member .photo{width:231px;height:257px;background:linear-gradient(160deg,#cfd6dc 0%,#9a8270 50%,#1f2328 100%)}
.member .photo.warm{background:linear-gradient(160deg,#3c2b1f 0%,#b88b5d 45%,#25201c 100%)}
.member .info{width:160px;padding-top:12px;border-top:1px solid var(--rule)}
.member h4{font-size:26px;font-weight:500;color:var(--ink);letter-spacing:1px}
.member .role{font-size:15px;color:#666;letter-spacing:1px;margin-top:4px;padding-bottom:18px;border-bottom:1px solid var(--rule)}
.member p{font-size:12px;line-height:24px;color:var(--muted);margin-top:14px}
.member .btn{width:150px;height:41px;font-size:15px;margin-top:18px}

.contact{left:0;top:2632px;width:1200px;height:475px;background:var(--dark)}
.request{left:84px;top:2692px;font-size:36px;font-weight:400;color:var(--white);line-height:50px}
.request em{font-style:normal;color:var(--blue)}
.request-rule{left:84px;top:2810px;width:110px;height:1px;background:#666}
.request-copy{left:84px;top:2825px;width:480px;font-size:18px;line-height:32px;color:#e5e5e5}
.info-box{left:86px;top:2929px;width:493px;height:130px;background:var(--darker);display:flex}
.info-item{flex:1;display:flex;gap:18px;padding:30px 20px;color:#eee;font-size:14px;line-height:24px}
.info-item + .info-item{border-left:1px solid #444}
.info-item b{font-weight:500;display:block}
.info-item svg{width:20px;height:20px;fill:none;stroke:#999;stroke-width:1.8;flex:none;margin-top:2px}
.divider{left:614px;top:2720px;width:1px;height:330px;background:#4a4a4a}
.field{border:1px solid #bdbdbd;color:#cfcfcf;font-size:14px;padding:0 20px;display:flex;align-items:center}
.f-name{left:651px;top:2716px;width:461px;height:48px}
.f-email{left:651px;top:2786px;width:215px;height:48px}
.f-phone{left:897px;top:2786px;width:215px;height:48px}
.f-msg{left:651px;top:2858px;width:461px;height:128px;align-items:flex-start;padding-top:16px}
.submit{left:651px;top:3010px;width:461px;height:48px;background:var(--blue);color:var(--white);font-size:19px;display:flex;align-items:center;justify-content:center}

.footer{left:0;top:3107px;width:1200px;height:107px;background:var(--footer)}
.footer-nav{left:0;width:1200px;top:3142px;display:flex;justify-content:center;font-size:14px;color:#ddd}
.footer-nav a{color:inherit;text-decoration:none;padding:0 40px;border-left:1px solid #555;line-height:14px}
.footer-nav a:first-child{border-left:0}
.copyright{left:0;width:1200px;top:3177px;text-align:center;font-size:11px;color:#666}
</style>
</head>
<body>

<div class="abs top-rule"></div>
<header class="abs header">
  <div class="abs brand"><span class="brand-name">Brightlane</span></div>
  <div class="abs header-contact">
    <span><svg viewBox="0 0 20 20"><circle cx="10" cy="10" r="10" fill="#2ea3dc"/><rect x="5" y="6.5" width="10" height="7" fill="none" stroke="#fff" stroke-width="1.4"/><path d="M5 7l5 4 5-4" fill="none" stroke="#fff" stroke-width="1.4"/></svg>hello@brightlane.example</span>
    <span><svg viewBox="0 0 20 20"><circle cx="10" cy="10" r="10" fill="#2ea3dc"/><rect x="7" y="5" width="6" height="10" rx="1" fill="none" stroke="#fff" stroke-width="1.4"/></svg>1-800-555-0142</span>
  </div>
  <div class="abs nav-line"></div>
  <nav class="abs nav"><a href="#">Home</a><a href="#">Vision</a><a href="#">Mission</a><a href="#">Team</a><a href="#">Contact</a></nav>
</header>

<div class="abs hero" role="img" aria-label="Photo of a team working at laptops in a bright open-plan office"></div>

<h1 class="abs section-title" style="top:835px;font-size:47px">Who we are</h1>
<div class="abs subtitle" style="top:907px"><i></i>Our vision<i></i></div>
<p class="abs lead" style="top:981px">We are a direct response company that creates and sells information products and services that millions of people find interesting and important in their lives.</p>
<p class="abs body-copy" style="top:1067px">We are specialized in the self-reliance market and we serve conservative Americans. We are in this business to serve globally and to grow individually. What we serve and inspire are people who need safety, comfort and peace of mind. We deliver empowerment through products that create fertile shortcuts to solutions, disentangle reality, simplify choices and ultimately make lives better. We give reassurance and confidence to these people through fresh, unique solutions.</p>
<a class="abs btn learn-more">Learn More</a>

<div class="abs values">
  <div class="value"><svg viewBox="0 0 62 62"><rect x="3" y="14" width="56" height="14" rx="7"/><rect x="3" y="36" width="56" height="14" rx="7"/></svg>Fairness</div>
  <div class="value"><svg viewBox="0 0 62 62"><path d="M31 44l-11-11a6 6 0 0 1 11-6 6 6 0 0 1 11 6z"/><path d="M6 30l10-14 10 4M56 32l-10 14-10-4"/></svg>Caring</div>
  <div class="value"><svg viewBox="0 0 62 62"><path d="M31 5l22 8v16c0 14-10 23-22 28C19 52 9 43 9 29V13z"/><path d="M31 11l16 6v12c0 10-7 17-16 21"/></svg>Safety</div>
  <div class="value"><svg viewBox="0 0 62 62"><path d="M31 20v34M31 20l-8 10M31 20l8 10M6 12l16 22 9-6 9 6 16-22"/></svg>Freedom</div>
  <div class="value"><svg viewBox="0 0 62 62"><circle cx="31" cy="31" r="26"/><path d="M31 27v17"/><circle cx="31" cy="19" r="1.5"/></svg>Help</div>
</div>

<div class="abs mission-photo" role="img" aria-label="Photo of a business handshake over a desk with documents and a laptop"></div>
<section class="abs mission-panel">
  <h2>What is it that we do?</h2>
  <h3>OUR MISSION</h3>
  <div class="rule"></div>
  <p>Lorem ipsum dolor sit amet, consectetur adipiscing elit, sed do eiusmod tempor incididunt ut labore et dolore magna aliqua. Ut enim ad minim veniam, quis nostrud exercitation ullamco laboris nisi ut aliquip ex ea commodo consequat.</p>
  <a class="btn">Learn More</a>
</section>

<h2 class="abs section-title" style="top:1996px;font-size:47px">Our Team &amp; Values</h2>
<div class="abs subtitle" style="top:2075px"><i></i>Our vision<i></i></div>
<p class="abs team-intro">We're a small team of smart, funny hard-working specialists who are pushing to become the #1 company in self-reliance. High ambition, radical honesty and a result-oriented mindset are encouraged at Brightlane.</p>

<article class="abs member" style="left:86px">
  <div class="photo" role="img" aria-label="Portrait photo of the CEO"></div>
  <div class="info">
    <h4>Marek Dorn</h4>
    <div class="role">CEO Brightlane</div>
    <p>Marek started or was involved in 15 failed businesses before discovering online copywriting.</p>
    <a class="btn">Learn More</a>
  </div>
</article>
<article class="abs member" style="left:624px">
  <div class="photo warm" role="img" aria-label="Portrait photo of the cofounder"></div>
  <div class="info">
    <h4>Elias Venn</h4>
    <div class="role">Cofounder</div>
    <p>Since the company's late 2012 start, Elias grew a network of 5000 affiliates.</p>
    <a class="btn">Learn More</a>
  </div>
</article>

<section class="abs contact"></section>
<h2 class="abs request">Request<br>Free <em>Appointment!</em></h2>
<div class="abs request-rule"></div>
<p class="abs request-copy">We are available to help you every step of the way with your construction project.</p>
<div class="abs info-box">
  <div class="info-item"><svg viewBox="0 0 20 20"><path d="M10 18s6-6 6-10a6 6 0 0 0-12 0c0 4 6 10 6 10z"/><circle cx="10" cy="8" r="2"/></svg><div><b>LOCATION</b>48 HARBOR ROW,<br>LAKEVIEW,</div></div>
  <div class="info-item"><svg viewBox="0 0 20 20"><rect x="2" y="2" width="16" height="16"/><path d="M6 6c0 5 3 8 8 8"/></svg><div><b>CONTACTS</b>555-010-2233<br>hello@brightlane.example</div></div>
</div>
<div class="abs divider"></div>
<div class="abs field f-name">Name...</div>
<div class="abs field f-email">Email...</div>
<div class="abs field f-phone">Phone No...</div>
<div class="abs field f-msg">Massege...</div>
<div class="abs submit">SUBMIT</div>

<footer class="abs footer"></footer>
<nav class="abs footer-nav"><a href="#">Home</a><a href="#">Vision</a><a href="#">Mission</a><a href="#">Team</a><a href="#">Contacts</a></nav>
<p class="abs copyright">© Copyright 2017 Brightlane All rights reserved</p>

</body>
</html>
```